The Willowmere Clinic Flyer Design

The Willowmere Clinic is a new company providing Dietetic services for people with gastrointestinal disorders. The main client base would be people suffering from Irritable Bowel Syndrome. IBS is a collection of symptoms which (will be individual to the suffer) including constipation/diarrhoea/abdominal pain or discomfort/bloating/belching/flatulence/stomach gurgling/reflux/nausea/urgency/incomplete emptying/fatigue/headaches. IBS affects approx 30% of the population. Previous treatments have generally been ineffectual and include medication, hypnotherapy, healthy eating.
Recently it has been found that the FODMAP diet (a diet low in fermentable Carbohydrates) has been effective in 75% of sufferers.
The Low FODMAP diet is complex and it is highly recommended that it is undertaken only under the supervision of a suitably qualified dietitian. Treatment is available within the QRV but is usually accessible only following consultation with a Gastroenterologist. Most GP's have never heard of this treatment as the research was only published in 2009 in Australia and is yet to filter through to the general practitioner. The Willowmere Clinic is the only clinic in the UK offering dietetic lead specialist services.
I am a member of the ZLO and MVRT (logos provided)
The flyer would be double sided, informing the patient of all the self help steps they could take if they have IBS then recommending that they contact The Willowmere Clinic for specialist advice.
Self Help: Healthy eating, regular meals, good intake of non caffeinated non alcoholic non fizzy drinks, regular exercise, stress management.
The flyer would be left in GP surgeries, Health centres, holistic therapy centres, or through doors.
Target Market(s)
Majority female aged 20-50, able to pay for private services
Industry/Entity Type
Clinic
Look and feel
Each slider illustrates characteristics of the customer's brand and the style your logo design should communicate.

```html
<!DOCTYPE html>
<html lang="en">
<head>
<meta charset="utf-8">
<title>The Willowmere Clinic – IBS Flyer</title>
<link rel="stylesheet" href="https://fonts.googleapis.com/css2?family=Roboto+Condensed:wght@300;400&family=Roboto:wght@300;400&display=swap">
<style>
  :root {
    --sky: #0cbbef;
    --sky-light: #8fd8f5;
    --navy: #0d4468;
    --ink-grey: #8a8a8c;
    --band: #3a3a3c;
    --card: #e6e6e7;
    --white: #ffffff;
  }
  * { box-sizing: border-box; margin: 0; padding: 0; }
  html, body { width: 1200px; height: 851px; overflow: hidden; background: var(--white); }
  .flyer { position: relative; width: 1200px; height: 851px; font-family: "Roboto", Arial, sans-serif; color: var(--ink-grey); }
  .abs { position: absolute; }

  .headline { left: 100px; top: 60px; font-family: "Roboto Condensed", sans-serif; font-weight: 300; font-size: 37px; color: #333; letter-spacing: 0.5px; }
  .intro { left: 100px; top: 117px; width: 468px; font-size: 14.5px; line-height: 19px; text-align: justify; font-weight: 300; }
  .intro p + p { margin-top: 19px; }

  .person-icon { left: 637px; top: 119px; width: 46px; height: 120px; background: var(--sky); border-radius: 23px 23px 6px 6px; }
  .stat { font-size: 14.5px; line-height: 19px; color: var(--sky); font-weight: 300; }
  .stat-proven { left: 696px; top: 119px; width: 143px; text-align: justify; }
  .stat-big { font-family: "Roboto Condensed", sans-serif; font-weight: 300; font-size: 50px; line-height: 48px; color: var(--navy); display: block; margin-top: 2px; }
  .stat-speed { left: 981px; top: 135px; width: 150px; }
  .stat-speed .stat-big { display: inline; }
  .chart-icon { left: 863px; top: 139px; }

  .detail { left: 100px; top: 270px; width: 1009px; font-size: 14.5px; line-height: 19px; text-align: justify; font-weight: 300; }

  .now-band { left: 0; top: 382px; width: 1200px; height: 56px; background: var(--band); }
  .now-tab { left: 0; top: 382px; }
  .now-label { left: 81px; top: 396px; font-family: "Roboto Condensed", sans-serif; font-weight: 300; font-size: 25px; color: var(--navy); }
  .now-text { left: 401px; top: 389px; width: 780px; font-size: 16.5px; line-height: 21px; color: var(--white); font-weight: 300; }

  .treatment-pill { left: 167px; top: 494px; width: 432px; height: 48px; background: var(--sky); border-radius: 10px; font-family: "Roboto Condensed", sans-serif; font-weight: 300; font-size: 23px; color: var(--navy); display: flex; align-items: center; justify-content: center; }

  .step { top: 580px; width: 205px; height: 205px; background: var(--card); border-radius: 14px; text-align: center; }
  .step-1 { left: 55px; } .step-2 { left: 280px; } .step-3 { left: 506px; }
  .step-num { position: absolute; left: 75px; top: 0; width: 55px; height: 54px; background: var(--white); border-radius: 0 0 10px 10px; font-family: "Roboto Condensed", sans-serif; font-size: 34px; color: var(--sky); line-height: 54px; }
  .step-text { position: absolute; left: 12px; right: 12px; top: 70px; font-size: 16.5px; line-height: 21.5px; font-weight: 300; color: var(--ink-grey); }

  .help-panel { left: 756px; top: 438px; width: 444px; height: 413px; background: var(--sky); }
  .help-arrow { left: 789px; top: 472px; }
  .help-title { left: 841px; top: 486px; font-family: "Roboto Condensed", sans-serif; font-weight: 300; font-size: 35px; line-height: 43px; color: var(--navy); }
  .help-call { left: 841px; top: 594px; font-family: "Roboto Condensed", sans-serif; font-weight: 300; font-size: 28px; line-height: 35px; color: var(--white); }
  .help-contact { left: 841px; top: 672px; font-family: "Roboto Condensed", sans-serif; font-weight: 300; font-size: 18.5px; line-height: 26px; color: var(--white); list-style: none; }
</style>
</head>
<body>
<main class="flyer">
  <h1 class="abs headline">DID YOU KNOW?</h1>
  <div class="abs intro">
    <p>IBS affects approx 30% of the population. Previous treatments have generally been ineffectual and include medication, hypnotherapy, healthy eating.</p>
    <p>Recently it has been found that the FODMAP diet (a diet low in fermentable Carbohydrates) has been effective in 75% of sufferers.</p>
  </div>

  <div class="abs person-icon" role="img" aria-label="Person pictogram"></div>
  <p class="abs stat stat-proven">Dietary treatment clinically proven to work in up to <span class="stat-big">75%</span>of patients.</p>

  <svg class="abs chart-icon" width="100" height="78" viewBox="0 0 100 78" aria-hidden="true">
    <path d="M2 4 V76 H98" fill="none" stroke="#0cbbef" stroke-width="4"/>
    <path d="M6 58 L16 44 L22 52 L30 38 L38 48 L46 36 L54 46 L64 30 L70 38 L84 18" fill="none" stroke="#0cbbef" stroke-width="6" stroke-linejoin="round"/>
    <path d="M74 10 L96 4 L90 26 Z" fill="#0cbbef"/>
  </svg>
  <p class="abs stat stat-speed">Results can be seen within<br><span class="stat-big">1-2</span> weeks.</p>

  <p class="abs detail">The Low FODMAP diet is complex and it is highly recommended that it is undertaken only under the supervision of a suitably qualified dietitian. Treatment is available within the QRV but is usually accessible only following consultation with a Gastroenterologist. Most GP's have never heard of this treatment as the research was only published in 2009 in Australia and is yet to filter through to the general practitioner. The Willowmere Clinic is the only clinic in the UK offering dietetic lead specialist services.</p>

  <div class="abs now-band"></div>
  <svg class="abs now-tab" width="362" height="56" viewBox="0 0 362 56" aria-hidden="true">
    <defs>
      <linearGradient id="nowGrad" x1="0" x2="1" y1="0" y2="0">
        <stop offset="0" stop-color="#9fdcf6"/>
        <stop offset="1" stop-color="#0cbbef"/>
      </linearGradient>
    </defs>
    <path d="M0 0 H305 L333 28 L305 56 H0 Z" fill="url(#nowGrad)"/>
    <path d="M305 0 L333 28 L305 56 L318 56 L346 28 L318 0 Z" fill="#222"/>
    <path d="M322 18 L340 28 L322 38 Z" fill="#0cbbef"/>
  </svg>
  <h2 class="abs now-label">WHAT TO DO NOW?</h2>
  <p class="abs now-text">Healthy eating, regular meals, good intake of non caffeinated non alcoholic non fizzy drinks, regular exercise, stress management</p>

  <h2 class="abs treatment-pill">WHAT’S INCLUDE IN THE TREATMENT?</h2>
  <section class="abs step step-1"><span class="step-num">1</span><p class="step-text">1 hour teaching session on the elimination phase, phone and e-mail support</p></section>
  <section class="abs step step-2"><span class="step-num">2</span><p class="step-text">1 hour appointment to teach the reintroduction phase</p></section>
  <section class="abs step step-3"><span class="step-num">3</span><p class="step-text">1 hour appointment to assess nutritional adequacy of the diet</p></section>

  <aside class="abs help-panel"></aside>
  <svg class="abs help-arrow" width="46" height="62" viewBox="0 0 46 62" aria-hidden="true">
    <path d="M10 2 V58 H44" fill="none" stroke="#0d4468" stroke-width="2"/>
    <path d="M1 12 L10 2 L19 12" fill="none" stroke="#0d4468" stroke-width="2"/>
  </svg>
  <h2 class="abs help-title">WHAT TO DO NEXT<br>IF THIS DOES NOT HELP?</h2>
  <p class="abs help-call">Please call or reach us<br>via information below:</p>
  <ul class="abs help-contact">
    <li>Tel: +83 562 7190</li>
    <li>Email: hello@willowmereclinic.com</li>
    <li>Website: www.willowmereclinic.com</li>
  </ul>
</main>
</body>
</html>
```